Website Design for a DJ Entertainment and Productions Comany

We are a full service DJ Entertainment and Productions company looking to have a strong presence in our local market and need a phenomenal website design to drive clients to the site but then also keep them there. We cater to all types of different events varying from weddings to proms to corporate events, birthdays, bar mitzvah's and so on and so on. We also do full lighting for any type of event and we also offer a photobooth service for various events. The best way to get an idea of the services that we offer is to visit http://www.velvarmusicworks.com/index.html This site is NOT our own but only linked as an example of what we do and will give you an overall overview of what we offer.
We are looking for pure creativity as there are multiple facets to our company and the services we offer. On the one hand we can provide a night club party atmosphere for Proms or dances but on the other hand we also provide professional full service emcee/DJ for weddings and formal events. The key for this site would be to have the pages for each category match the look and feel of the actual service provided, ie the Wedding page will look more refined and professional vs the Party DJ page. Each page needs to fit the overall feel of the Company and Logo though. Here is a list of pages that we would need to have on the final site.
HOME PAGE
PROFESSINAL DJS- This will have info. and pricing of our DJ services for everything but weddings. Should have pics and videos somewhere on this page.
WEDDINGS- All wedding package pricing and info. This page should look more elegant, formal and high class compared to the other pages.
PHOTOBOOTH-Page with info, pricing on photobooth see http://www.glimmerboxkiosk.com/
LIGHTING DESIGN-Info on our lighting services along with pricing
CORPORATE EVENTS-Info on services and pricing for corporate events. This page should seem more professional centered towards business clientele.
CLIENT LOGIN-Page for existing clients to logon to update info and fill out information.
CONNECT WITH US- Social Media links.
Our logo was submitted through Pixel Forum but I am open to suggestions on revisions if you feel the need to change it. Color is also not set in stone.
Updates
I have increased my budget $200 more. Please submit your designs for review, deadline is approaching quickly. Also see brief for revisions.
Thank you.
Target Market(s)
Broad Range but usually Under 40
Industry/Entity Type
Night Club
Look and feel

```html
<!DOCTYPE html>
<html lang="en">
<head>
<meta charset="utf-8">
<title>Kestrel Entertainment &amp; Productions</title>
<link href="https://fonts.googleapis.com/css2?family=Questrial&display=swap" rel="stylesheet">
<style>
:root{
  --bg:#000;
  --glow:#0c0a5a;
  --red:#d4141c;
  --red-dark:#7c0a0e;
  --white:#f2f2f2;
  --grey:#9a9a9a;
  --nav:#e6e6e6;
}
*{margin:0;padding:0;box-sizing:border-box}
html,body{width:1200px;height:753px;overflow:hidden;background:var(--bg)}
body{font-family:"Questrial",sans-serif;color:var(--white)}
.page{position:relative;width:1200px;height:753px;overflow:hidden;
  background:linear-gradient(90deg,#000 0,#000 150px,#05042a 175px,var(--glow) 220px,#0a0848 380px,#05042a 470px,#000 525px,#000 100%);}
.brand{position:absolute;left:128px;top:20px;display:flex;align-items:center;gap:12px;color:var(--red)}
.brand-mark{width:68px;height:68px;border-radius:50%;background:var(--red)}
.brand-name{font-size:34px;line-height:1;letter-spacing:1px}
.brand-name small{display:block;font-size:10.5px;letter-spacing:.3px;margin-top:4px}
.cta{position:absolute;left:838px;top:23px;width:235px;height:52px;border:2px solid var(--red);border-radius:8px;
  background:linear-gradient(#a1121a,var(--red-dark));color:#ff3b3b;text-align:center;padding-top:7px;text-decoration:none}
.cta strong{display:block;font-size:20px;letter-spacing:.5px;font-weight:400}
.cta span{display:block;font-size:10px;letter-spacing:.6px;color:#ff6a6a}
.nav{position:absolute;left:281px;top:88px;display:flex;gap:23px;list-style:none}
.nav a{color:var(--nav);font-size:12px;letter-spacing:1.4px;text-decoration:none}
.services{position:absolute;left:179px;top:140px;display:grid;grid-template-columns:repeat(3,253px);column-gap:35px;row-gap:44px}
.service{text-align:center}
.service-photo{width:253px;height:170px}
.service-title{margin-top:12px;font-size:17px;letter-spacing:.3px;font-weight:400}
.ph-dj{background:linear-gradient(135deg,#3a4452,#9aa0a6 45%,#2b2f35)}
.ph-wed{background:linear-gradient(180deg,#c9d7df,#8fa4b1 55%,#2e3338)}
.ph-booth{background:linear-gradient(90deg,#c8202c,#e3a6b0 40%,#f3eef0 70%,#b88894)}
.ph-light{background:radial-gradient(ellipse at 35% 35%,#e6f21a,#37c23c 35%,#5b1c8a 60%,#050505 85%)}
.ph-corp{background:linear-gradient(135deg,#c9aaa0,#7a3a32 45%,#1b1b24 70%)}
.ph-event{background:linear-gradient(180deg,#b9b3a8,#e9e6df 45%,#2d3f66 80%)}
.footer{position:absolute;left:95px;top:650px;width:975px}
.phone{font-size:20px;color:var(--grey)}
.phone a{color:var(--red);text-decoration:none;margin-left:14px}
.legal{margin-top:8px;font-size:13px;color:var(--grey)}
.legal a{color:var(--red);text-decoration:none}
.like{position:absolute;left:339px;top:18px;display:flex;align-items:center;gap:6px;font-size:10px}
.like-btn{display:flex;align-items:center;gap:3px;height:18px;padding:0 6px;background:#3a3a3a;border:1px solid #555;border-radius:2px;color:#999}
.like-count{background:#ddd;color:#333;padding:1px 6px}
.social{position:absolute;right:0;top:15px;display:flex;gap:10px;list-style:none}
.social li{width:28px;height:28px;border-radius:4px;background:var(--red);border:1px solid #ff4040}
</style>
</head>
<body>
<div class="page">
  <div class="brand">
    <div class="brand-mark"></div>
    <div class="brand-name">KESTREL<small>ENTERTAINMENT &amp; PRODUCTIONS</small></div>
  </div>
  <a class="cta" href="#"><strong>BUILD YOUR PARTY</strong><span>PACKAGES AND PRICING</span></a>
  <ul class="nav">
    <li><a href="#">PROFESSIONAL DJS</a></li>
    <li><a href="#">WEDDINGS</a></li>
    <li><a href="#">PHOTOBOOTH</a></li>
    <li><a href="#">LIGHTING DESIGN</a></li>
    <li><a href="#">CORPORATE EVENTS</a></li>
    <li><a href="#">EVENT DESIGN</a></li>
  </ul>
  <div class="services">
    <div class="service"><div class="service-photo ph-dj" role="img" aria-label="DJ hands on a mixer and turntable"></div><h2 class="service-title">PROFESSIONAL DJS</h2></div>
    <div class="service"><div class="service-photo ph-wed" role="img" aria-label="Turntable with a wedding couple dancing behind"></div><h2 class="service-title">WEDDINGS</h2></div>
    <div class="service"><div class="service-photo ph-booth" role="img" aria-label="Stack of photobooth prints of guests"></div><h2 class="service-title">PHOTOBOOTH</h2></div>
    <div class="service"><div class="service-photo ph-light" role="img" aria-label="Laser and stage lights over a crowd"></div><h2 class="service-title">LIGHTING DESIGN</h2></div>
    <div class="service"><div class="service-photo ph-corp" role="img" aria-label="Businessman holding a glass of red wine"></div><h2 class="service-title">CORPORATE EVENTS</h2></div>
    <div class="service"><div class="service-photo ph-event" role="img" aria-label="Banquet hall set with tables and flowers"></div><h2 class="service-title">EVENT DESIGN</h2></div>
  </div>
  <div class="footer">
    <p class="phone">555.014.0362 &bull; <a href="#">CLIENT LOG IN</a></p>
    <p class="legal">&copy; Kestrel Entertainment &amp; Productions &bull; <a href="#">CONTACT</a></p>
    <div class="like">
      <span class="like-btn"><svg width="9" height="8" viewBox="0 0 9 8"><path d="M1 4l2.5 2.5L8 1" stroke="#999" stroke-width="1.6" fill="none"/></svg>Like</span>
      <span class="like-count">2</span>
    </div>
    <ul class="social"><li></li><li></li><li></li></ul>
  </div>
</div>
</body>
</html>
```